Flyer Design Project

I need a flyer design to pass out to promote my business and to bring in more business. My business is a auto body shop and we do auto body repair on all makes and models. We take all types of insurance work and cash deals are welcome. We type of paint we use is KVX so i would like the KVX logo somewhere on the flyer.I would also like to include that we offer free estimates.
Updates

I forgot to include the following information to my shop

Address : 3846 N. Willowmere Ave
                 San Mateo, Ca 94402

Tel : 650-817-3926

Website : www.KelvoCollision.com

please include that cash deals are welcome, we offer 24 hours drop off service, and we offer mobile estimate service

Industry/Entity Type

Insurance

Requirements
Must have
• Must have my company logo in it. Must be eye catching.

```html
<!DOCTYPE html>
<html lang="en">
<head>
<meta charset="utf-8">
<title>Kelvo Collision – Flyer</title>
<link href="https://fonts.googleapis.com/css2?family=Cinzel:wght@700&family=Lato:wght@400;700;900&display=swap" rel="stylesheet">
<style>
  :root {
    --stage: #e9e6e2;
    --charcoal: #1b1d21;
    --orange: #f26a1b;
    --red: #b71f26;
    --white: #ffffff;
    --ink: #2a2a2a;
  }
  * { margin: 0; padding: 0; box-sizing: border-box; }
  html, body { width: 1200px; height: 886px; overflow: hidden; background: var(--stage); }
  .canvas { position: relative; width: 1200px; height: 886px; }
  .flyer {
    position: absolute; left: 300px; top: 23px; width: 600px; height: 840px;
    overflow: hidden; font-family: "Lato", sans-serif; color: var(--white);
    background: #1c1b1c;
    box-shadow: 0 6px 24px rgba(0,0,0,.25);
  }
  .flyer-art { position: absolute; inset: 0; }
  .brand {
    position: absolute; left: 34px; top: 48px; display: flex; align-items: center; gap: 12px;
    font-weight: 900; font-size: 34px; letter-spacing: .5px; color: var(--white);
  }
  .brand-dot { width: 22px; height: 22px; border-radius: 50%; background: var(--red); }
  .services { position: absolute; left: 40px; top: 236px; }
  .services-title { font-family: "Cinzel", serif; font-size: 22px; letter-spacing: 1px; margin-bottom: 6px; }
  .services-list { list-style: none; }
  .services-list li { position: relative; padding-left: 22px; font-size: 13px; line-height: 17px; }
  .services-list li::before {
    content: ""; position: absolute; left: 3px; top: 2px; width: 6px; height: 10px;
    border-right: 3px solid var(--orange); border-bottom: 3px solid var(--orange);
    transform: rotate(40deg);
  }
  .offer {
    position: absolute; left: 355px; top: 168px; width: 215px; text-align: center;
    font-weight: 700; font-size: 27px; line-height: 32px;
  }
  .offer .highlight { color: var(--orange); }
  .contact-band {
    position: absolute; left: -10px; top: 772px; width: 680px; height: 72px;
    transform: rotate(-13deg); transform-origin: left top;
    background: linear-gradient(90deg, #c02128 0%, #9a1a20 70%, #3e1013 100%);
    display: flex; align-items: center; gap: 26px; padding-left: 30px;
  }
  .address { font-size: 16px; line-height: 20px; white-space: nowrap; }
  .phone { font-weight: 900; font-size: 28px; white-space: nowrap; }
  .website {
    position: absolute; left: 452px; top: 650px; font-weight: 700; font-size: 13px; color: var(--ink);
    transform: rotate(-13deg); transform-origin: left top; white-space: nowrap;
  }
</style>
</head>
<body>
<div class="canvas">
  <article class="flyer">
    <svg class="flyer-art" width="600" height="840" viewBox="0 0 600 840">
      <defs>
        <linearGradient id="bodyFill" x1="0" y1="0" x2="0" y2="1">
          <stop offset="0" stop-color="#242323"/>
          <stop offset=".25" stop-color="#4a4440"/>
          <stop offset=".6" stop-color="#5c534d"/>
          <stop offset="1" stop-color="#2a2828"/>
        </linearGradient>
        <linearGradient id="panelFill" x1="0" y1="0" x2="0" y2="1">
          <stop offset="0" stop-color="#2c2f35"/>
          <stop offset="1" stop-color="#121316"/>
        </linearGradient>
        <linearGradient id="carFill" x1="0" y1="0" x2="1" y2="1">
          <stop offset="0" stop-color="#3a3d42"/>
          <stop offset=".5" stop-color="#0e0f11"/>
          <stop offset="1" stop-color="#55585d"/>
        </linearGradient>
        <linearGradient id="workshopFill" x1="0" y1="0" x2="1" y2="1">
          <stop offset="0" stop-color="#c9c2b8"/>
          <stop offset="1" stop-color="#b5322e"/>
        </linearGradient>
        <linearGradient id="damageFill" x1="0" y1="0" x2="1" y2="1">
          <stop offset="0" stop-color="#d8d9db"/>
          <stop offset="1" stop-color="#2b2e33"/>
        </linearGradient>
      </defs>

      <rect class="base" width="600" height="840" fill="url(#bodyFill)"/>
      <path class="header-sweep" d="M0 0H600V80C470 120 330 150 200 175 120 190 50 205 0 215Z" fill="#1f1e1f"/>
      <path class="accent-line" d="M0 218C120 195 330 160 600 95" stroke="var(--orange)" stroke-width="3" fill="none"/>
      <path class="lower-shade" d="M0 505C120 530 220 550 320 590V840H0Z" fill="#1c1b1c"/>
      <path class="accent-line" d="M0 505C120 530 230 555 330 600" stroke="var(--orange)" stroke-width="3" fill="none"/>

      <path class="offer-panel" d="M330 260A125 125 0 0 1 600 245V700H330Z" fill="url(#panelFill)"/>

      <path class="car-photo" role="img" aria-label="Photo of a glossy black luxury coupe, front three-quarter view"
            d="M240 580C320 500 440 465 600 455V760H240Z" fill="url(#carFill)"/>

      <path class="white-swoosh" d="M600 260C560 420 520 580 340 720L600 660Z" fill="var(--white)"/>

      <circle class="photo-ring" role="img" aria-label="Photo of a technician painting a red car in the workshop"
              cx="190" cy="590" r="58" fill="url(#workshopFill)" stroke="var(--orange)" stroke-width="6"/>
      <circle class="photo-ring" role="img" aria-label="Photo of a damaged black car awaiting repair"
              cx="160" cy="692" r="48" fill="url(#damageFill)" stroke="var(--orange)" stroke-width="6"/>
    </svg>

    <div class="brand"><span class="brand-dot"></span>Kelvo Collision</div>

    <section class="services">
      <h2 class="services-title">SERVICES:</h2>
      <ul class="services-list">
        <li>Collision Repairs</li>
        <li>All Insurance Work Accepted</li>
        <li>Major and minor accident damage repair</li>
        <li>All Foreign and Domestic makes and models</li>
        <li>Exact frame straightening on premises</li>
        <li>Expert paint matching and refinishing</li>
        <li>Paintless dent repair</li>
        <li>Free damage repair estimates</li>
        <li>Bumper spot refinishing</li>
        <li>Windshield Replacement</li>
        <li>Expert Unibody Reconstruction</li>
        <li>Dent Removal</li>
        <li>Car Detailing</li>
      </ul>
    </section>

    <p class="offer">Cash deals are welcome, we offer <span class="highlight">24 hours</span> drop off service, and we offer mobile estimate service</p>

    <p class="website">www.KelvoCollision.com</p>
    <div class="contact-band">
      <p class="address">3846 N. Willowmere Ave<br>San Mateo, Ca 94402</p>
      <p class="phone">Tel : 650-817-3926</p>
    </div>
  </article>
</div>
</body>
</html>
```